Life Coach for Lawyers Business Card Design

Elegant, original, business card design for life coaching service for associate attorneys who work in big law and struggle with stress, overwhelm, and time management. Double sided design.

Target Market(s)

Women associate attorneys who work in big law and struggle with stress, overwhelm, and time management.

Industry/Entity Type

Life Coaching

Contact Information for Business Card

Marissa Pendrell
Life Coach
518.677.3941
calmbriefcounsel.net
marissa@calmbriefcounsel.net
@calmbriefcounsel (Instagram)

Font styles to use
Other font styles liked:
• Silver South font duo. See uploaded files.

Requirements
Must have
• Icons for phone, website, email, and Instagram instead of words. Specific colors used in my logo (171B2B, 421121, FFFFFF)
Nice to have
• Foil. Embossed. Feminine design.
Should not have
• Any colors other than those used in logo. See uploaded files.

```html
<!DOCTYPE html>
<html lang="en">
<head>
<meta charset="utf-8">
<title>Calm Brief Counsel – Business Card</title>
<link href="https://fonts.googleapis.com/css2?family=Allison&family=Playfair+Display:wght@500&display=swap" rel="stylesheet">
<style>
  :root {
    --ink: #171B2B;
    --wine: #421121;
    --paper: #FFFFFF;
    --edge: #B5B5B8;
    --rule: #C9C9CC;
    --script: "Allison", cursive;
    --serif: "Playfair Display", serif;
  }
  * { margin: 0; padding: 0; box-sizing: border-box; }
  html, body {
    width: 1200px;
    height: 353px;
    overflow: hidden;
    background: var(--paper);
  }
  .sheet {
    position: relative;
    width: 1200px;
    height: 353px;
  }
  .card {
    position: absolute;
    top: 12px;
    width: 556px;
    height: 330px;
    background: var(--paper);
    border: 1px solid var(--edge);
    overflow: hidden;
  }
  .card--front { left: 13px; }
  .card--back { left: 632px; }

  .corner-band {
    position: absolute;
    right: 0;
    bottom: 0;
    width: 232px;
    height: 30px;
    background: var(--wine);
    border-top-left-radius: 30px;
  }

  .brand {
    position: absolute;
    color: var(--wine);
    font-family: var(--serif);
    font-weight: 500;
    line-height: 1;
    text-transform: uppercase;
  }
  .brand__top { display: block; }
  .brand__main { display: block; }

  .card--front .brand {
    left: 56px;
    top: 150px;
    width: 220px;
    text-align: center;
  }
  .card--front .brand__top { font-size: 17px; letter-spacing: 5px; margin-bottom: 4px; }
  .card--front .brand__main { font-size: 40px; letter-spacing: 4px; }

  .divider {
    position: absolute;
    left: 294px;
    top: 130px;
    width: 1px;
    height: 68px;
    background: var(--rule);
  }

  .identity {
    position: absolute;
    left: 316px;
    top: 136px;
  }
  .identity__name {
    font-family: var(--script);
    font-size: 34px;
    color: var(--wine);
    line-height: 1;
    white-space: nowrap;
  }
  .identity__role {
    font-size: 22px;
    color: var(--ink);
  }
  .identity__phone {
    margin-top: 6px;
    font-family: var(--script);
    font-size: 28px;
    color: var(--ink);
    line-height: 1;
  }

  .card--back .brand {
    left: 56px;
    top: 84px;
    width: 170px;
    text-align: center;
  }
  .card--back .brand__top { font-size: 13px; letter-spacing: 4px; margin-bottom: 3px; }
  .card--back .brand__main { font-size: 31px; letter-spacing: 3px; }

  .back-rule {
    position: absolute;
    left: 56px;
    top: 147px;
    width: 80px;
    height: 1px;
    background: var(--rule);
  }

  .contacts {
    position: absolute;
    left: 56px;
    top: 164px;
    list-style: none;
  }
  .contact {
    display: flex;
    align-items: center;
    height: 32px;
  }
  .contact__icon {
    width: 16px;
    height: 16px;
    margin-right: 9px;
    flex: none;
  }
  .contact__text {
    font-family: var(--script);
    font-size: 26px;
    color: var(--ink);
    line-height: 1;
  }
</style>
</head>
<body>
<main class="sheet">

  <section class="card card--front" aria-label="Card front">
    <div class="brand">
      <span class="brand__top">Calm Brief</span>
      <span class="brand__main">Counsel</span>
    </div>
    <div class="divider"></div>
    <div class="identity">
      <p class="identity__name">Marissa Pendrell <span class="identity__role">- life coach</span></p>
      <p class="identity__phone">518 677 3941</p>
    </div>
    <div class="corner-band"></div>
  </section>

  <section class="card card--back" aria-label="Card back">
    <div class="brand">
      <span class="brand__top">Calm Brief</span>
      <span class="brand__main">Counsel</span>
    </div>
    <div class="back-rule"></div>
    <ul class="contacts">
      <li class="contact">
        <svg class="contact__icon" viewBox="0 0 16 16" aria-hidden="true">
          <rect x="0" y="0" width="16" height="16" rx="3" fill="#EFE7EA"/>
          <rect x="3" y="4.5" width="10" height="7" rx="1" fill="none" stroke="#421121" stroke-width="1.2"/>
          <path d="M3.5 5 L8 8.5 L12.5 5" fill="none" stroke="#421121" stroke-width="1.2"/>
        </svg>
        <span class="contact__text">marissa@calmbriefcounsel.net</span>
      </li>
      <li class="contact">
        <svg class="contact__icon" viewBox="0 0 16 16" aria-hidden="true">
          <rect x="0" y="0" width="16" height="16" rx="3" fill="#EFE7EA"/>
          <circle cx="8" cy="8" r="5" fill="none" stroke="#421121" stroke-width="1.1"/>
          <ellipse cx="8" cy="8" rx="2.2" ry="5" fill="none" stroke="#421121" stroke-width="1"/>
          <path d="M3 8 H13" stroke="#421121" stroke-width="1"/>
        </svg>
        <span class="contact__text">calmbriefcounsel.net</span>
      </li>
      <li class="contact">
        <svg class="contact__icon" viewBox="0 0 16 16" aria-hidden="true">
          <rect x="0" y="0" width="16" height="16" rx="3" fill="#EFE7EA"/>
          <rect x="4" y="4" width="8" height="8" fill="none" stroke="#421121" stroke-width="1.2"/>
        </svg>
        <span class="contact__text">@calmbriefcounsel</span>
      </li>
    </ul>
    <div class="corner-band"></div>
  </section>

</main>
</body>
</html>
```